Infographic for explaining evidence based medicine

I need 2 diagrams for a talking I am doing later this week . The purpose of the talk is to explain the current approach to evidence based medicine and then the approach of utilising big data. The talk is to doctors who are considered experts in their field. I have attached the layout of the diagrams. Everything on them in italics is just notes. I am really just looking to stylise the people, add in some colours and make it look better than mine. There will be minimal changes.

Target Market(s)

Doctors - considered experts in their field

Industry/Entity Type

Medical And Science

Font styles to use
Serif
Sans Serif

Requirements
Must have
• Quick turn around. Simple design. Needs to make my pictures look better then I have done them.
• Need the colours as described - basicially red, orange and green people

```html
<!DOCTYPE html>
<html lang="en">
<head>
<meta charset="utf-8">
<title>Evidence Based Medicine – Treatment Outcomes</title>
<link rel="stylesheet" href="https://fonts.googleapis.com/css2?family=Montserrat:wght@600&display=swap">
<style>
  :root {
    --bg: #ffffff;
    --ink: #111111;
    --line: #1a1a1a;
    --orange: #f79a55;
    --orange-deep: #c85a0e;
    --green: #14a77c;
    --green-deep: #267a68;
    --red: #e03a2f;
    --red-deep: #931615;
    --pill-bg: #f7f7f7;
    --pill-ring: #e8e8e8;
    --pill-white: #ececec;
    --pill-green: #22ab82;
    --pill-blue: #06b8e0;
  }
  html, body {
    margin: 0;
    padding: 0;
    width: 1200px;
    height: 675px;
    overflow: hidden;
    background: var(--bg);
  }
  .diagram {
    display: block;
    width: 1200px;
    height: 675px;
  }
  .connector {
    stroke: var(--line);
    stroke-width: 1.2;
    fill: none;
  }
  .choice-disc {
    fill: var(--pill-bg);
    stroke: var(--pill-ring);
    stroke-width: 1.5;
  }
  .patient { stroke: var(--bg); stroke-width: 1.5; }
  .patient--orange { fill: url(#tone-orange); }
  .patient--green { fill: url(#tone-green); }
  .patient--red { fill: url(#tone-red); }
  .or-label {
    font-family: "Montserrat", sans-serif;
    font-weight: 600;
    font-size: 33px;
    fill: var(--ink);
  }
</style>
</head>
<body>
<svg class="diagram" viewBox="0 0 1200 675" xmlns="http://www.w3.org/2000/svg">
  <defs>
    <linearGradient id="tone-orange" x1="0" y1="0" x2="0" y2="1">
      <stop offset="0.48" stop-color="var(--orange)"/>
      <stop offset="0.48" stop-color="var(--orange-deep)"/>
    </linearGradient>
    <linearGradient id="tone-green" x1="0" y1="0" x2="0" y2="1">
      <stop offset="0.48" stop-color="var(--green)"/>
      <stop offset="0.48" stop-color="var(--green-deep)"/>
    </linearGradient>
    <linearGradient id="tone-red" x1="0" y1="0" x2="0" y2="1">
      <stop offset="0.48" stop-color="var(--red)"/>
      <stop offset="0.48" stop-color="var(--red-deep)"/>
    </linearGradient>
    <linearGradient id="capsule-green" x1="0" y1="0" x2="1" y2="0">
      <stop offset="0.5" stop-color="var(--pill-white)"/>
      <stop offset="0.5" stop-color="var(--pill-green)"/>
    </linearGradient>
    <linearGradient id="capsule-blue" x1="0" y1="0" x2="1" y2="0">
      <stop offset="0.5" stop-color="var(--pill-white)"/>
      <stop offset="0.5" stop-color="var(--pill-blue)"/>
    </linearGradient>
  </defs>

  <!-- Patient population -->
  <g class="population" role="img" aria-label="Crowd of patients: thirteen orange, eleven green and two red figures">
    <g class="row row--back">
      <rect class="patient patient--orange" x="143" y="136" width="52" height="170" rx="12"/>
      <rect class="patient patient--orange" x="192" y="136" width="52" height="170" rx="12"/>
      <rect class="patient patient--orange" x="244" y="136" width="52" height="170" rx="12"/>
      <rect class="patient patient--orange" x="295" y="134" width="52" height="172" rx="12"/>
      <rect class="patient patient--orange" x="343" y="136" width="52" height="170" rx="12"/>
      <rect class="patient patient--orange" x="396" y="136" width="52" height="170" rx="12"/>
    </g>
    <g class="row row--second">
      <rect class="patient patient--orange" x="104" y="194" width="52" height="180" rx="12"/>
      <rect class="patient patient--orange" x="160" y="194" width="52" height="180" rx="12"/>
      <rect class="patient patient--orange" x="214" y="194" width="52" height="180" rx="12"/>
      <rect class="patient patient--orange" x="270" y="194" width="52" height="180" rx="12"/>
      <rect class="patient patient--orange" x="328" y="194" width="52" height="180" rx="12"/>
      <rect class="patient patient--orange" x="382" y="194" width="52" height="180" rx="12"/>
      <rect class="patient patient--orange" x="436" y="194" width="52" height="180" rx="12"/>
    </g>
    <g class="row row--third">
      <rect class="patient patient--green" x="96" y="260" width="52" height="192" rx="12"/>
      <rect class="patient patient--green" x="152" y="260" width="52" height="192" rx="12"/>
      <rect class="patient patient--green" x="210" y="260" width="52" height="192" rx="12"/>
      <rect class="patient patient--green" x="266" y="260" width="52" height="192" rx="12"/>
      <rect class="patient patient--green" x="320" y="260" width="52" height="192" rx="12"/>
      <rect class="patient patient--green" x="378" y="258" width="52" height="194" rx="12"/>
      <rect class="patient patient--green" x="440" y="258" width="52" height="194" rx="12"/>
    </g>
    <g class="row row--front">
      <rect class="patient patient--green" x="145" y="312" width="52" height="192" rx="12"/>
      <rect class="patient patient--red" x="224" y="316" width="56" height="214" rx="12"/>
      <rect class="patient patient--red" x="282" y="316" width="56" height="214" rx="12"/>
      <rect class="patient patient--green" x="362" y="312" width="52" height="192" rx="12"/>
    </g>
  </g>

  <!-- Branching connectors from population -->
  <path class="connector" d="M494 326 H532 M532 188 V475 M532 188 H580 M532 475 H580"/>

  <!-- Treatment A -->
  <circle class="choice-disc" cx="654" cy="190" r="74"/>
  <rect class="treatment-icon" x="610" y="176" width="96" height="27" rx="13.5"
        fill="url(#capsule-green)" role="img" aria-label="Capsule, treatment A"/>

  <!-- Treatment B -->
  <circle class="choice-disc" cx="654" cy="490" r="74"/>
  <rect class="treatment-icon" x="610" y="479" width="96" height="27" rx="13.5"
        fill="url(#capsule-blue)" role="img" aria-label="Capsule, treatment B"/>

  <text class="or-label" x="645" y="348" text-anchor="middle">OR</text>

  <!-- Outcome connectors -->
  <path class="connector" d="M729 190 H824 M824 78 V302 M824 78 H872 M824 190 H872 M824 302 H872"/>
  <path class="connector" d="M729 492 H824 M824 380 V605 M824 380 H872 M824 492 H872 M824 605 H872"/>

  <!-- Outcomes, treatment A -->
  <g class="outcome" role="img" aria-label="Seven green patients">
    <rect class="patient patient--green" x="880" y="40" width="21" height="82" rx="5"/>
    <rect class="patient patient--green" x="905" y="40" width="21" height="82" rx="5"/>
    <rect class="patient patient--green" x="930" y="40" width="21" height="82" rx="5"/>
    <rect class="patient patient--green" x="955" y="40" width="21" height="82" rx="5"/>
    <rect class="patient patient--green" x="981" y="40" width="21" height="82" rx="5"/>
    <rect class="patient patient--green" x="1006" y="40" width="21" height="82" rx="5"/>
    <rect class="patient patient--green" x="1031" y="40" width="21" height="82" rx="5"/>
  </g>
  <g class="outcome" role="img" aria-label="Four orange patients">
    <rect class="patient patient--orange" x="880" y="146" width="21" height="82" rx="5"/>
    <rect class="patient patient--orange" x="905" y="146" width="21" height="82" rx="5"/>
    <rect class="patient patient--orange" x="930" y="146" width="21" height="82" rx="5"/>
    <rect class="patient patient--orange" x="955" y="146" width="21" height="82" rx="5"/>
  </g>
  <g class="outcome" role="img" aria-label="One red patient">
    <rect class="patient patient--red" x="881" y="246" width="21" height="82" rx="5"/>
  </g>

  <!-- Outcomes, treatment B -->
  <g class="outcome" role="img" aria-label="Two green patients">
    <rect class="patient patient--green" x="880" y="342" width="21" height="82" rx="5"/>
    <rect class="patient patient--green" x="905" y="342" width="21" height="82" rx="5"/>
  </g>
  <g class="outcome" role="img" aria-label="Nine orange patients">
    <rect class="patient patient--orange" x="880" y="448" width="21" height="82" rx="5"/>
    <rect class="patient patient--orange" x="905" y="448" width="21" height="82" rx="5"/>
    <rect class="patient patient--orange" x="930" y="448" width="21" height="82" rx="5"/>
    <rect class="patient patient--orange" x="955" y="448" width="21" height="82" rx="5"/>
    <rect class="patient patient--orange" x="981" y="448" width="21" height="82" rx="5"/>
    <rect class="patient patient--orange" x="1006" y="448" width="21" height="82" rx="5"/>
    <rect class="patient patient--orange" x="1031" y="448" width="21" height="82" rx="5"/>
    <rect class="patient patient--orange" x="1056" y="448" width="21" height="82" rx="5"/>
    <rect class="patient patient--orange" x="1081" y="448" width="21" height="82" rx="5"/>
  </g>
  <g class="outcome" role="img" aria-label="One red patient">
    <rect class="patient patient--red" x="881" y="549" width="21" height="82" rx="5"/>
  </g>
</svg>
</body>
</html>
```